Summit Glossfloor & Honing
I'm looking for a business card and logo design for my
new Polished Concrete & Grinding business,
If you were to look up Summit in the dictionary it would
say, first in importance, order, or position; leading.
Polished Concrete floors are a niche market, that are being used currently in Shopping centres, office spaces and by most high end architects, builders and designers.
i need my business card & logo to stand out from my
competitors, i need my design + logo to reflect this it
needs to be simple, professional, eye catching, easy
to read and scream quality. The logo will need to be
suitable for a whole range of applications including,
uniforms, letter heads, stickers, and eventually
incorporating in vehicle vinyl wrapping.
Target Market(s)
Builders, architects, Interior designers & home owners
Contact Information for Business Card
Front side:
- Summit Glossfloor & Honing.
- Logo
Rear side:
- Liam Varga
- 0491735082
- info@summitgfh.com.au
- commercial - domestic - industrial
- (later down the line website & space for
social media links
www.summitglossfloor.com.au)
Colors
Designer to choose colors to be used in the design.
Look and feel

```html
<!DOCTYPE html>
<html lang="en">
<head>
<meta charset="utf-8">
<title>Summit Glossfloor &amp; Honing – Business Card</title>
<link rel="stylesheet" href="https://fonts.googleapis.com/css2?family=Exo+2:wght@700&family=Arimo:wght@400&display=swap">
<style>
  :root {
    --brand-blue: #0eaddc;
    --brand-blue-deep: #0a9cc9;
    --soft-grey: #c9cacc;
    --text-grey: #6f7275;
    --card-white: #ffffff;
    --backdrop: #2b2b2d;
  }
  * { box-sizing: border-box; margin: 0; padding: 0; }
  html, body { width: 1200px; height: 880px; overflow: hidden; }
  body {
    background: var(--backdrop);
    font-family: "Arimo", Arial, sans-serif;
    position: relative;
  }
  .card {
    position: absolute;
    left: 290px;
    width: 620px;
    height: 354px;
    border-radius: 22px;
    background: var(--card-white);
    overflow: hidden;
    box-shadow: 0 14px 30px rgba(0,0,0,.45);
  }
  .card--front { top: 66px; }
  .card--back { top: 460px; }
  .card__art { position: absolute; inset: 0; width: 620px; height: 354px; }

  .logo {
    position: absolute;
    display: flex;
    align-items: center;
    gap: 14px;
  }
  .logo__mark {
    width: 34px; height: 34px;
    border-radius: 50%;
    background: var(--brand-blue);
    flex: none;
  }
  .logo__name {
    font-family: "Exo 2", Arial, sans-serif;
    font-weight: 700;
    color: var(--brand-blue);
    line-height: 1.05;
  }
  .card--front .logo { left: 120px; top: 128px; }
  .card--front .logo__name { font-size: 34px; }
  .card--back .logo { left: 46px; top: 168px; }
  .card--back .logo__mark { width: 26px; height: 26px; }
  .card--back .logo__name { font-size: 24px; }

  .holder {
    position: absolute;
    left: 46px; top: 252px;
    font-family: "Exo 2", Arial, sans-serif;
    font-weight: 700;
    font-size: 21px;
    color: var(--brand-blue);
  }
  .contacts {
    position: absolute;
    left: 46px; top: 288px;
    list-style: none;
    font-size: 12.5px;
    color: var(--text-grey);
  }
  .contacts li { display: flex; align-items: center; gap: 8px; height: 19px; }
  .contacts svg { width: 14px; height: 14px; flex: none; }

  .services {
    position: absolute;
    right: 34px; top: 196px;
    list-style: none;
    text-align: right;
    font-size: 13px;
    color: var(--text-grey);
  }
  .services li { height: 19px; display: flex; justify-content: flex-end; align-items: center; gap: 8px; }
  .services li::after {
    content: ""; width: 6px; height: 6px; border-radius: 50%;
    background: var(--brand-blue);
  }
</style>
</head>
<body>

<section class="card card--front" aria-label="Card front">
  <svg class="card__art" viewBox="0 0 620 354" aria-hidden="true">
    <path d="M620 82 C 540 220, 330 300, 0 316 L0 330 C 340 318, 560 236, 620 112 Z" fill="var(--soft-grey)"/>
    <path d="M620 112 C 560 236, 340 318, 0 330 L0 354 L620 354 Z" fill="var(--brand-blue)"/>
  </svg>
  <div class="logo">
    <span class="logo__mark"></span>
    <span class="logo__name">Summit Glossfloor<br>&amp; Honing</span>
  </div>
</section>

<section class="card card--back" aria-label="Card back">
  <svg class="card__art" viewBox="0 0 620 354" aria-hidden="true">
    <path d="M0 0 H620 V182 C 470 70, 200 60, 0 130 Z" fill="var(--brand-blue)"/>
    <path d="M0 130 C 200 60, 470 70, 620 182 V204 C 470 92, 210 86, 0 146 Z" fill="var(--soft-grey)"/>
    <path d="M0 146 C 210 86, 470 92, 620 204 V214 C 470 104, 210 98, 0 156 Z" fill="var(--card-white)"/>
    <g fill="none" stroke="#fff" stroke-width="2">
      <circle cx="462" cy="40" r="14"/>
      <circle cx="500" cy="40" r="14"/>
      <circle cx="538" cy="40" r="14"/>
      <circle cx="576" cy="40" r="14"/>
    </g>
    <line x1="46" y1="280" x2="586" y2="280" stroke="var(--brand-blue)" stroke-width="1"/>
  </svg>

  <div class="logo">
    <span class="logo__mark"></span>
    <span class="logo__name">Summit Glossfloor<br>&amp; Honing</span>
  </div>

  <p class="holder">Liam Varga</p>

  <ul class="contacts">
    <li>
      <svg viewBox="0 0 14 14"><circle cx="7" cy="7" r="6.3" fill="none" stroke="var(--brand-blue)"/><rect x="4.8" y="3.4" width="4.4" height="7.2" rx="0.8" fill="none" stroke="var(--brand-blue)"/></svg>
      0491735082
    </li>
    <li>
      <svg viewBox="0 0 14 14"><circle cx="7" cy="7" r="6.3" fill="var(--brand-blue)"/><rect x="3.6" y="4.8" width="6.8" height="4.6" fill="#fff"/><path d="M3.6 4.8 L7 7.4 L10.4 4.8" fill="none" stroke="var(--brand-blue)" stroke-width="0.8"/></svg>
      info@summitgfh.com.au
    </li>
    <li>
      <svg viewBox="0 0 14 14"><circle cx="7" cy="7" r="6.3" fill="none" stroke="var(--brand-blue)"/><circle cx="7" cy="7" r="3.6" fill="none" stroke="var(--brand-blue)" stroke-width="0.8"/><path d="M3.4 7 H10.6 M7 3.4 V10.6" stroke="var(--brand-blue)" stroke-width="0.8"/></svg>
      www.summitglossfloor.com.au
    </li>
  </ul>

  <ul class="services">
    <li>Commercial</li>
    <li>Domestic</li>
    <li>Industrial</li>
  </ul>
</section>

</body>
</html>
```